Brindlecombe Couriers/Brindlecombe Self-storage Awareness A5 leaflet

We run two companies here in the UK: Brindlecombe Couriers and Brindlecombe self-Storage. We would like an A5 leaflet with a company on each side. Brindlecombe couriers focuses on urgent deliveries and delivers all over the UK and Europe. Brindlecombe Self-storage offers storage to anyone that needs it. We would like both sides to relate to their respective websites (www.brindlecombecouriers.co.uk and www.brindlecombeselfstorage.co.uk) so please use information from their homepages. We do not want too much information on either side, the main goal is to deliver these locally just to let people know we are here. We occupy a large blue warehouse so perhaps a cartoon-style blue warehouse could work but isn't required. A small map on the brindlecombe storage side is ideal and contact info should be kept to a minimum but is required. Please include on the couriers side that we support 'Lantern of kindness' and on the Brindlecombe Self storage side that we support 'Harrowfield Carelink'. I have included as many images as possible. Do not feel the need to include them all.

Target Market(s)

Local individuals.

Font styles to use
Sans Serif

Colors
0355a3

Requirements
Must have
• logos
• charity supports (lantern of kindness - couriers, harrowfield carelink - Selfstorage)
• not cluttered with information.
• Selfstorage - self storage, business storage, distribution, and serviced offices for hire.
• Couriers - deliver 24 hours a day, 7 days a week. Same day, next day deliveries, light removals.
• follow colour schemes of websites. dark blue, yellow, lime green, white.
• relate to it's website.
Nice to have
• map on the Brindlecombe Self Storage side.
• a notice that we have offices available for rent on the Brindlecombe Self storage side.
• couriers side focuses on the fact we make urgent deliveries.
• not much white.
Should not have
• more than a couple of photographs.
• too much writing

```html
<!DOCTYPE html>
<html lang="en">
<head>
<meta charset="utf-8">
<title>Brindlecombe leaflets</title>
<link rel="stylesheet" href="https://fonts.googleapis.com/css2?family=Ubuntu:ital,wght@0,500;0,700;1,500;1,700&display=swap">
<style>
  :root{
    --bg:#e3e7e7;
    --white:#ffffff;
    --storage-blue:#1f52e8;
    --logo-blue:#0355a3;
    --navy:#141c7e;
    --lime:#9be31a;
    --orange:#f5a414;
    --red:#e5231f;
  }
  html,body{margin:0;padding:0;overflow:hidden;}
  body{width:1200px;height:1200px;background:var(--bg);font-family:"Ubuntu",sans-serif;position:relative;}
  .leaflet{position:absolute;top:218px;width:540px;height:764px;background:var(--white);box-shadow:0 10px 30px rgba(0,0,0,.18);overflow:hidden;}
  .leaflet--storage{left:40px;}
  .leaflet--couriers{left:620px;}
  .leaflet svg.shapes{position:absolute;inset:0;width:540px;height:764px;}
  .brand{position:absolute;top:22px;left:30px;display:flex;align-items:center;gap:8px;font-weight:700;font-size:18px;color:var(--logo-blue);}
  .brand__mark{width:14px;height:14px;background:var(--logo-blue);}
  .services{position:absolute;left:30px;margin:0;padding:0;list-style:none;}
  .services li{display:flex;align-items:center;gap:12px;color:var(--white);font-weight:700;font-size:25px;line-height:36px;}
  .services li::before{content:"";width:26px;height:7px;border-radius:4px;transform:skewX(-20deg);}
  .leaflet--storage .services{top:336px;}
  .leaflet--storage .services li::before{background:var(--lime);}
  .leaflet--couriers .services{top:368px;}
  .leaflet--couriers .services li::before{background:var(--orange);}
  .badge{position:absolute;width:132px;height:132px;border-radius:50%;background:var(--lime);display:flex;align-items:center;justify-content:center;text-align:center;}
  .badge::after{content:"";position:absolute;inset:7px;border:3px solid var(--white);border-radius:50%;}
  .badge__text{color:var(--white);font-weight:700;font-size:19px;line-height:22px;transform:rotate(18deg);}
  .leaflet--storage .badge{left:378px;top:400px;}
  .leaflet--couriers .badge{left:384px;top:440px;}
  .contact{position:absolute;left:30px;margin:0;padding:0;list-style:none;font-weight:700;font-style:italic;font-size:12px;line-height:18px;}
  .contact li{display:flex;align-items:center;gap:6px;white-space:nowrap;}
  .contact svg{width:11px;height:11px;flex:none;}
  .leaflet--storage .contact{top:596px;color:var(--logo-blue);}
  .leaflet--couriers .contact{top:606px;color:var(--navy);}
  .contact .indent{padding-left:17px;}
  .supporters{position:absolute;right:26px;bottom:16px;display:flex;align-items:center;gap:8px;white-space:nowrap;}
  .supporters__label{color:var(--lime);font-weight:700;font-style:italic;font-size:13px;}
  .supporters__name{font-weight:700;font-size:14px;}
  .leaflet--storage .supporters__name{color:#c4247a;}
  .leaflet--couriers .supporters__name{color:#8dc63f;}
</style>
</head>
<body>

<section class="leaflet leaflet--storage" aria-label="Brindlecombe Self Storage leaflet">
  <svg class="shapes" viewBox="0 0 540 764">
    <defs>
      <linearGradient id="corridor" x1="0" y1="0" x2="1" y2="0">
        <stop offset="0" stop-color="#2b3568"/>
        <stop offset=".5" stop-color="#8c8a70"/>
        <stop offset="1" stop-color="#2c3560"/>
      </linearGradient>
    </defs>
    <polygon role="img" aria-label="Photo of a storage corridor lined with blue containers" points="0,52 300,62 540,132 540,340 0,300" fill="url(#corridor)"/>
    <polygon points="300,62 540,120 540,132 310,72" fill="var(--lime)"/>
    <polygon points="0,296 540,330 540,590 0,545" fill="var(--storage-blue)"/>
    <polygon points="0,290 540,322 540,336 0,306" fill="var(--lime)"/>
    <polygon points="296,596 522,618 514,712 288,690" fill="var(--lime)"/>
    <polygon points="303,604 514,624 507,704 296,684" fill="var(--storage-blue)"/>
    <polygon role="img" aria-label="Street map showing the storage site location" points="309,610 508,629 502,698 302,679" fill="#e9edf0"/>
  </svg>
  <div class="brand"><span class="brand__mark"></span>Brindlecombe Self Storage</div>
  <ul class="services">
    <li>Self Storage</li>
    <li>Business Storage</li>
    <li>Distribution</li>
    <li>Serviced Offices for hire</li>
  </ul>
  <div class="badge"><span class="badge__text">Offices<br>Available<br>for Rent</span></div>
  <ul class="contact">
    <li><svg viewBox="0 0 12 12"><path d="M2 1h3l1 3-2 1a7 7 0 0 0 3 3l1-2 3 1v3c-6 0-10-4-10-9z" fill="var(--lime)"/></svg>01632 960 418</li>
    <li><svg viewBox="0 0 12 12"><rect x="1" y="2" width="10" height="8" fill="var(--lime)"/><path d="M1 2l5 4 5-4" stroke="#fff" fill="none"/></svg>info@brindlecombeselfstorage.co.uk</li>
    <li><svg viewBox="0 0 12 12"><path d="M6 1a4 4 0 0 1 4 4c0 3-4 7-4 7S2 8 2 5a4 4 0 0 1 4-4z" fill="var(--lime)"/></svg>Brindlecombe Self Storage</li>
    <li class="indent">The Carriage Yard, Fenwick Lane</li>
    <li class="indent">Brindlecombe, Kent, BR14 6QT</li>
  </ul>
  <div class="supporters"><span class="supporters__label">proud supporters of</span><span class="supporters__name">Harrowfield Carelink</span></div>
</section>

<section class="leaflet leaflet--couriers" aria-label="Brindlecombe Couriers leaflet">
  <svg class="shapes" viewBox="0 0 540 764">
    <defs>
      <linearGradient id="van" x1="0" y1="0" x2="0" y2="1">
        <stop offset="0" stop-color="#3a55a8"/>
        <stop offset=".55" stop-color="#dfe3ea"/>
        <stop offset="1" stop-color="#7c7f86"/>
      </linearGradient>
      <linearGradient id="staff" x1="0" y1="0" x2="1" y2="1">
        <stop offset="0" stop-color="#d8d6cf"/>
        <stop offset=".6" stop-color="#3b57b0"/>
        <stop offset="1" stop-color="#2a2a30"/>
      </linearGradient>
    </defs>
    <polygon role="img" aria-label="Photo of a white courier van parked by blue containers" points="0,56 540,70 540,368 0,330" fill="url(#van)"/>
    <polygon points="200,72 540,96 540,112 240,84" fill="var(--red)"/>
    <polygon points="0,318 540,356 540,600 0,560" fill="var(--navy)"/>
    <polygon points="0,312 300,330 540,366 540,380 300,344 0,328" fill="var(--orange)"/>
    <polygon points="304,600 522,620 514,716 296,696" fill="var(--lime)"/>
    <polygon points="294,588 510,606 506,628 290,610" fill="var(--red)"/>
    <polygon points="290,588 304,588 296,696 282,696" fill="var(--red)"/>
    <polygon role="img" aria-label="Photo of two staff members handling parcels in the office" points="310,606 508,626 502,708 302,690" fill="url(#staff)"/>
  </svg>
  <div class="brand"><span class="brand__mark"></span>Brindlecombe Couriers</div>
  <ul class="services">
    <li>24 Hours a Day</li>
    <li>7 Days a Week</li>
    <li>Same Day Deliveries</li>
    <li>Next Day Deliveries</li>
    <li>Light Removals</li>
  </ul>
  <div class="badge"><span class="badge__text">“Dedicated<br>to<br>Deliver”</span></div>
  <ul class="contact">
    <li><svg viewBox="0 0 12 12"><path d="M2 1h3l1 3-2 1a7 7 0 0 0 3 3l1-2 3 1v3c-6 0-10-4-10-9z" fill="var(--orange)"/></svg>01632 960 275</li>
    <li><svg viewBox="0 0 12 12"><rect x="1" y="2" width="10" height="8" fill="var(--orange)"/><path d="M1 2l5 4 5-4" stroke="#fff" fill="none"/></svg>info@brindlecombecouriers.co.uk</li>
    <li><svg viewBox="0 0 12 12"><path d="M6 1a4 4 0 0 1 4 4c0 3-4 7-4 7S2 8 2 5a4 4 0 0 1 4-4z" fill="var(--orange)"/></svg>Brindlecombe Self Storage</li>
    <li class="indent">The Carriage Yard, Fenwick Lane</li>
    <li class="indent">Brindlecombe, Kent, BR14 6QT</li>
  </ul>
  <div class="supporters"><span class="supporters__label">proud supporters of</span><span class="supporters__name">Lantern of kindness</span></div>
</section>

</body>
</html>
```